Design new Brackwater Asset business card 2016

We need a new business card for our company Brackwater Asset Partners. We are a niche Alternative Investment Fund Manager based in Chester, in the North West of the UK.We market our services to global institutions such as banks, insurance companies, pension funds, etc. as well as wealthy individuals. Our main markets are Europe (Germany\France\Switzerland), the US and parts of Asia.
The design needs to be in line with existing company branding. Life the assets we deal with, the business card might suggest, "niche\alternative" type of attributes - however, it needs to remain professional, clean and appropriate for our client base.
Our existing business card format with relevant factual information is included, along with logo and branding details.

Target Market(s)

We market our services to global institutions such as banks, insurance companies, pension funds, etc. as well as wealthy individuals.

Industry/Entity Type

Financial Service

Contact Information for Business Card

please see attached pdf for information on existing business card which we should aim to convey on your new design. However:
- the wording "Brackwater Asset Partners Ltd is Authorised and Regulated
by the Monetary Oversight Bureau. Registered No. 7139046" should be replaced with , "Brackwater Asset Partners Ltd is an Alternative Investment Fund Manager Authorised and Regulated by the Monetary Oversight Bureau. Registered No. 7139046"
- the "reception" word on reverse can be omitted.
- the "retail: www.toplivanex.co.uk" wording can be omitted.
- the QR code is not required in the new version.

Font styles to use
Serif
Sans Serif

Requirements
Must have
• information on current business card, subject to comments provided above.
Nice to have
• Use of areas of solid colour instead of large areas of white space might be nice to experiment with. However, still need to have the general look and feel of the brand as presented on our website www.bwfundco.co.uk
• If we had space for 3 bullet points describing what we do\who we are, this might be good to try out. e.g. alternative investment fund manager, longevity specialist, founded 1990.
• Also, we have a new tag line, "expertise with longevity" which might fit nicely somewhere on the business card.
Should not have
• - no QR code
• - should not use all the colours in our logo as it looks very garish! Using one or two colours with black\white etc, seems to work better.

```html
<!DOCTYPE html>
<html lang="en">
<head>
<meta charset="utf-8">
<title>Brackwater Asset Partners – Business Cards</title>
<link rel="stylesheet" href="https://fonts.googleapis.com/css2?family=Libre+Baskerville&family=Raleway:wght@400&display=swap">
<style>
  :root {
    --backdrop: #3b3b3c;
    --card-light: #f4f4f4;
    --card-mid: #e4e4e5;
    --pattern: #d9d9db;
    --brand-brown: #5b3b22;
    --mark-gold: #c9a43a;
    --accent-blue: #29a8df;
    --accent-yellow: #f7bc1e;
    --legal-grey: #6a6a6a;
  }
  * { margin: 0; padding: 0; box-sizing: border-box; }
  html, body {
    width: 1200px;
    height: 667px;
    overflow: hidden;
  }
  body {
    background: var(--backdrop);
    display: flex;
    align-items: center;
    justify-content: center;
    gap: 60px;
  }
  .card {
    position: relative;
    width: 500px;
    height: 300px;
    background: linear-gradient(135deg, var(--card-light) 0%, var(--card-mid) 100%);
    overflow: hidden;
    box-shadow: 0 6px 18px rgba(0,0,0,0.35);
  }
  .card__pattern {
    position: absolute;
    left: 0;
    top: 0;
    width: 62%;
    height: 100%;
    background: radial-gradient(ellipse at 30% 40%, var(--pattern) 0%, rgba(217,217,219,0) 70%);
  }
  .card__accent {
    position: absolute;
    inset: 0;
    width: 100%;
    height: 100%;
  }
  .brand {
    position: absolute;
    left: 0;
    right: 0;
    top: 42px;
    display: flex;
    flex-direction: column;
    align-items: center;
    gap: 16px;
  }
  .brand__dot {
    width: 76px;
    height: 76px;
    border-radius: 50%;
    background: var(--mark-gold);
  }
  .brand__name {
    font-family: "Libre Baskerville", serif;
    font-size: 24px;
    color: var(--brand-brown);
    letter-spacing: 0.5px;
  }
  .legal {
    position: absolute;
    left: 96px;
    top: 238px;
    width: 320px;
    font-family: "Raleway", sans-serif;
    font-size: 9px;
    line-height: 1.45;
    color: var(--legal-grey);
  }
</style>
</head>
<body>

  <div class="card card--swoosh">
    <div class="card__pattern" role="img" aria-label="Faint grey mosaic pattern"></div>
    <svg class="card__accent" viewBox="0 0 500 300" aria-hidden="true">
      <path d="M500,100 C495,200 450,270 368,300 L500,300 Z" fill="var(--accent-yellow)"/>
      <path d="M500,120 C496,212 462,274 396,300 L500,300 Z" fill="var(--accent-blue)"/>
    </svg>
    <div class="brand">
      <span class="brand__dot"></span>
      <span class="brand__name">Brackwater Asset Partners</span>
    </div>
    <p class="legal">Brackwater Asset Partners Ltd is Authorised and Regulated<br>by the Monetary Oversight Bureau. Registered No. 7139046</p>
  </div>

  <div class="card card--squares">
    <div class="card__pattern" role="img" aria-label="Faint grey mosaic pattern"></div>
    <svg class="card__accent" viewBox="0 0 500 300" aria-hidden="true">
      <rect x="441" y="244" width="59" height="56" fill="var(--accent-blue)"/>
      <rect x="418" y="228" width="64" height="62" fill="var(--accent-yellow)"/>
    </svg>
    <div class="brand">
      <span class="brand__dot"></span>
      <span class="brand__name">Brackwater Asset Partners</span>
    </div>
    <p class="legal">Brackwater Asset Partners Ltd is Authorised and Regulated<br>by the Monetary Oversight Bureau. Registered No. 7139046</p>
  </div>

</body>
</html>
```